Online trading school - Website design

We are building an online trading school (trading of shares, commodities, indices, currencies). The purpose is to teach online traders how to trade successfully. We need to design the homepage of the website and logo (plomavurn.com will be the domain). The homepage will contain the following elements

- logo
- Sign in and Register links/buttons
- upper menu
- short introduction
- a couple of bullet points 'Why to join our school?'
- sign up form
- text
- bottom menu

Attached is a draft for the designer. The draft is just for an inspiration, the actual structure of the website can be different if the designer thinks so.

The designer is free to choose colors.

School

3 page

```html
<!DOCTYPE html>
<html lang="en">
<head>
<meta charset="utf-8">
<title>Plomavurn – Trading Glossary</title>
<link href="https://fonts.googleapis.com/css2?family=Open+Sans:wght@400;600&family=Roboto+Condensed:wght@400;700&family=Ubuntu:wght@700&display=swap" rel="stylesheet">
<style>
  :root{
    --orange:#f47b20;
    --blue:#2f80c4;
    --blue-dark:#1f6aa8;
    --term:#1d6fb4;
    --ink:#222;
    --text:#333;
    --grey:#555;
    --footer:#1b1b1b;
    --footer-deep:#111;
    --white:#fff;
  }
  *{box-sizing:border-box;margin:0;padding:0}
  html,body{width:858px;height:1200px;overflow:hidden;background:var(--white)}
  body{position:relative;font-family:"Open Sans",Arial,sans-serif;color:var(--text)}
  .top-rule{position:absolute;top:0;left:0;width:858px;height:2px;background:var(--orange)}
  .brand{position:absolute;left:70px;top:18px;font-family:"Ubuntu",Arial,sans-serif;font-weight:700;font-size:30px;color:#3a3a3a;letter-spacing:.3px}
  .account{position:absolute;top:2px;right:71px;display:flex}
  .account a{display:block;height:25px;line-height:25px;font-size:8.5px;font-weight:600;color:var(--white);text-decoration:none;text-align:center}
  .sign-in{width:72px;background:#222;margin-right:4px}
  .register{width:72px;background:var(--orange)}
  .follow{position:absolute;top:42px;right:70px;display:flex;align-items:center;font-size:8.5px;color:var(--grey)}
  .follow span{margin-right:8px}
  .follow i{display:block;width:18px;height:18px;border-radius:50%;background:#7b7b7b;margin-left:4px}
  .main-nav{position:absolute;top:72px;left:0;width:858px;height:34px;background:var(--blue);border-bottom:1px solid var(--blue-dark)}
  .main-nav ul{list-style:none;display:flex;margin-left:70px;height:100%}
  .main-nav li{height:100%;border-right:1px solid var(--blue-dark);font-size:9px;color:var(--white);display:flex;align-items:center;justify-content:center}
  .main-nav li.active{background:var(--orange);border-right-color:var(--orange)}
  .glossary{position:absolute;left:70px;top:136px;width:482px}
  .glossary h1{font-family:"Roboto Condensed",Arial,sans-serif;font-weight:400;font-size:21px;color:var(--ink);margin-bottom:5px}
  .glossary p{font-size:8.6px;line-height:14.5px;margin-bottom:9.5px}
  .glossary b{font-family:"Roboto Condensed",Arial,sans-serif;font-weight:400;font-size:10px;color:var(--term)}
  .join{position:absolute;left:581px;top:140px;width:206px;height:203px;background:var(--blue);padding:16px 17px}
  .join h2{font-family:"Roboto Condensed",Arial,sans-serif;font-weight:400;font-size:16px;color:var(--white);margin-bottom:11px}
  .join .field{height:27px;background:var(--white);border:1px solid #d7e4ef;margin-bottom:4px;font-size:8px;color:#666;padding:0 8px;line-height:27px}
  .agree{display:flex;align-items:center;font-size:8.5px;color:var(--white);margin-top:8px}
  .agree i{width:9px;height:9px;background:var(--white);margin-right:5px}
  .agree u{margin-left:3px}
  .join .submit{margin-top:10px;width:82px;height:24px;background:var(--orange);color:var(--white);font-family:"Roboto Condensed",Arial,sans-serif;font-size:10px;line-height:24px;text-align:center}
  .site-footer{position:absolute;left:0;top:1081px;width:858px;height:63px;background:var(--footer)}
  .footer-brand{position:absolute;left:70px;top:15px;font-family:"Ubuntu",Arial,sans-serif;font-weight:700;font-size:25px;color:var(--white)}
  .newsletter{position:absolute;left:282px;top:23px;font-family:"Roboto Condensed",Arial,sans-serif;font-size:13px;color:var(--white)}
  .subscribe{position:absolute;left:463px;top:18px;width:324px;height:28px;border-radius:14px;background:var(--white);overflow:hidden}
  .subscribe span{position:absolute;left:18px;top:0;line-height:28px;font-size:8.5px;color:#777}
  .subscribe .go{position:absolute;right:0;top:0;width:49px;height:28px;background:var(--orange);color:var(--white);font-family:"Roboto Condensed",Arial,sans-serif;font-size:13px;line-height:28px;text-align:center;padding-right:6px}
  .legal{position:absolute;left:0;top:1144px;width:858px;height:56px;background:var(--footer-deep);border-top:1px solid #2a2a2a;text-align:center;font-size:8.5px;line-height:15px;color:var(--white);padding-top:16px}
</style>
</head>
<body>
  <div class="top-rule"></div>
  <div class="brand">Plomavurn</div>
  <div class="account"><a class="sign-in">SIGN IN</a><a class="register">REGISTER</a></div>
  <div class="follow"><span>Follow Us</span><i></i><i></i><i></i></div>

  <nav class="main-nav">
    <ul>
      <li style="width:62px">HOME</li>
      <li style="width:132px">ABOUT OUR SCHOOL</li>
      <li style="width:102px">RISK WARNING</li>
      <li style="width:57px">FAQ</li>
      <li class="active" style="width:125px">TRADING GLOSSARY</li>
      <li style="width:90px">CONTACT US</li>
    </ul>
  </nav>

  <main class="glossary">
    <h1>GLOSSARY OF TERMS</h1>
    <p>With online trading you will definitely come in handy this list, which contains simple and concise definitions of basic and most used terms</p>
    <p><b>SHARES</b> - identification of the security that is associated with the right owner to participate in the management of the company, on its property, profit, etc.</p>
    <p><b>ASK</b> - demand price that is available to the trader to purchase one of business tools.</p>
    <p><b>BACKTEST</b> - authentication business strategies according to records from the past. Trader avoids the risk of losing money by testing their strategies already known data.</p>
    <p><b>BID</b> - bid price, a trader tries to redeem a financial instrument.</p>
    <p><b>BROKER</b> - demand price that is available to the trader to purchase one of business tools.</p>
    <p><b>CASH FLOW</b> - the difference between income and expenditure of funds for a certain period.</p>
    <p><b>CFD - CONTRACT FOR DIFFERENCE</b> - contracts for differences. It is a contract between two parties, which commands the purchaser to pay the difference between the current value and the price at a predetermined time. It enables the investor to benefit from a rise or fall in prices without real ownership of the instrument.</p>
    <p><b>DAY TRADING</b> - investing in one day. Positions instruments opens and closes in a short timeframe.</p>
    <p><b>LONG POSITION</b>- a situation where the investor has purchased a financial instrument, and expects it to grow at market price.</p>
    <p><b>EMISSIONS</b> - regarding the issue of securities, thus exposing them to publish and put into circulation. Carried out directly by or through banks.</p>
    <p><b>EQUITY - ASSETS</b> - the value of funds on the trading account after deduction of profits and losses from an active business</p>
    <p><b>LEVERAGE</b> - a mechanism that allows trading order more capital than is in the account. The ratio between fair trade and total. The ratio also represents a potential value gain or loss.</p>
    <p><b>FOREX - FOREIGN EXCHANGE MARKET</b> - an abbreviation of Foreign Exchange. The largest OTC market with its own rules as a day of engagement.</p>
    <p><b>FUNDAMENT, FUNDAMENTAL NEWS</b> - information that affects the development of prices on the stock exchange. Their publication could result in unexpected behavior of the market.</p>
    <p><b>GAP</b> - it is a big jump in prices, which usually occurs over the weekend. It may be addicted to unexpected economic or geopolitical events. It can be described as the price gap between the opening and closing exchanges.</p>
    <p><b>INDICATOR</b> - an auxiliary tool in trading platforms, which is used to correct the timing of entry to a specific position.</p>
    <p><b>INSIDER TRADING</b> - trading on the basis of reliable information obtained under the internal structure of the company or the state. It brings great benefit when trading in the market.</p>
    <p><b>PRINCIPAL</b> - borrowed sum. Borrower applies for the loan of this amount pay creditors.</p>
    <p><b>COMMODITIES</b> - Major instruments (grain, precious metals, oil, etc.), which today serves mainly as a means to deal with derivatives (futures, options, etc.).</p>
    <p><b>SHORT POSITION</b> - a situation where an investor sold a financial instrument and expects to increase it at market price.</p>
    <p><b>LOT</b> - a fixed amount of a particular tradable asset. It is buying and selling units, which establishes an exchange or broker.</p>
    <p><b>MACRODATA</b> - regular reports announced within individual economies. Affect prices on the current and future market.</p>
    <p><b>SHORT POSITION</b> - a situation where an investor sold a financial instrument and expects to increase it at market price.</p>
    <p><b>MARGIN - MARGIN</b> - the amount required to open a trading position. When using financial leverage is necessary to count with sufficient capital to cover potential losses in the value of the ratio of the volume of trade.</p>
  </main>

  <aside class="join">
    <h2>JOIN OUR SCHOOL NOW!</h2>
    <div class="field">First Name</div>
    <div class="field">Last Name</div>
    <div class="field">Email</div>
    <div class="agree"><i></i>Agree with our<u>terms and Conditions</u></div>
    <div class="submit">SIGN UP</div>
  </aside>

  <footer class="site-footer">
    <div class="footer-brand">Plomavurn</div>
    <div class="newsletter">NEWSLETTER SUBSCRIPTION</div>
    <div class="subscribe"><span>Enter your Email</span><div class="go">GO</div></div>
  </footer>
  <div class="legal">Terms and Conditions / Privacy protection<br>© Copyright 2016 Plomavurn . All Rights Reserved.</div>
</body>
</html>
```